Valtoria - Managed Service Provider Brochure

Our company has launched a new division, a "Managed Service Provider (MSP)" division and we are looking for a new bifold brochure to market our company.
This new service provides our clients a vendor management solution to save money and control their procurement process. We would like to maintain the same color scheme of black and red as the core colors along our logo.
We have provided a recent powerpoint presentation done by our team containing the copy material that can be used for this project. We do not require the images stay the same so feel free to incorporate what works best in the design.
Thank you.
It Company

```html
<!DOCTYPE html>
<html lang="en">
<head>
<meta charset="utf-8">
<title>Valtoria – Vendor Management Program Brochure</title>
<link rel="stylesheet" href="https://fonts.googleapis.com/css2?family=Raleway:wght@500;600;700&family=Open+Sans:wght@400;600&display=swap">
<style>
  :root {
    --red: #e0474f;
    --red-deep: #cf4049;
    --charcoal: #4a4a4d;
    --charcoal-dark: #3a3a3d;
    --paper: #ffffff;
    --ink: #3b3b3e;
    --stage: #ece9e2;
    --sky-light: #a9c6e0;
    --sky-dark: #2e3d57;
    --office-light: #d9dde2;
    --office-mid: #a9afb8;
  }
  * { margin: 0; padding: 0; box-sizing: border-box; }
  html, body { width: 1200px; height: 800px; overflow: hidden; background: var(--stage); }
  .canvas { position: relative; width: 1200px; height: 800px; }

  .spread {
    position: absolute; left: 100px; top: 50px;
    width: 1000px; height: 700px;
    display: flex;
    box-shadow: 0 14px 34px rgba(0,0,0,.18);
  }
  .panel { position: relative; width: 500px; height: 700px; background: var(--paper); overflow: hidden; }
  .panel svg.shapes { position: absolute; inset: 0; width: 500px; height: 700px; }

  /* Back panel */
  .cta-block {
    position: absolute; left: 0; top: 0; width: 290px; height: 170px;
    background: var(--red);
    padding: 52px 0 0 40px;
  }
  .cta-text {
    font-family: "Raleway", sans-serif; font-weight: 600;
    color: var(--paper); font-size: 19px; line-height: 1.2;
    text-transform: uppercase; letter-spacing: .5px;
  }
  .meeting-photo {
    position: absolute; left: 0; top: 170px; width: 500px; height: 530px;
    background: linear-gradient(160deg, var(--sky-light) 0%, #6f8db0 40%, var(--sky-dark) 100%);
  }
  .contact-column {
    position: absolute; left: 290px; top: 120px; width: 210px; height: 440px;
    background: rgba(58,58,61,.9);
    padding: 38px 16px 0 22px;
    font-family: "Open Sans", sans-serif; color: #e6e6e6;
    font-size: 10.5px; line-height: 1.65; white-space: nowrap;
  }
  .contact-column .label { font-weight: 600; color: var(--paper); }
  .contact-heading { font-weight: 600; color: var(--paper); margin-bottom: 2px; }
  .url-tag {
    display: inline-block; background: var(--red); color: var(--paper);
    font-family: "Open Sans", sans-serif; font-weight: 600;
    font-size: 10px; padding: 3px 10px;
  }
  .contact-column .url-tag { margin-top: 14px; }

  .brand { position: absolute; font-family: "Raleway", sans-serif; color: var(--ink); }
  .brand-name { display: flex; align-items: center; gap: 8px; font-weight: 600; letter-spacing: .5px; }
  .brand-mark { display: inline-block; background: var(--red); }
  .brand-tagline { font-family: "Open Sans", sans-serif; font-weight: 600; color: var(--ink); }

  .brand--back { left: 318px; top: 38px; }
  .brand--back .brand-name { font-size: 24px; }
  .brand--back .brand-mark { width: 10px; height: 10px; }
  .brand--back .brand-tagline { font-size: 7px; margin-top: 2px; }

  /* Front panel */
  .team-photo {
    position: absolute; left: 0; top: 0; width: 500px; height: 400px;
    background: linear-gradient(135deg, var(--office-light) 0%, #c4c9cf 55%, var(--office-mid) 100%);
  }
  .front-url { position: absolute; left: 22px; top: 22px; }
  .program-title {
    position: absolute; left: 52px; top: 322px;
    font-family: "Raleway", sans-serif; font-weight: 600;
    color: var(--paper); font-size: 34px; line-height: 1.08;
    letter-spacing: 2px; text-transform: uppercase;
    transform: rotate(24.7deg); transform-origin: left top;
    white-space: nowrap;
  }
  .brand--front { left: 40px; top: 628px; }
  .brand--front .brand-name { font-size: 36px; }
  .brand--front .brand-mark { width: 13px; height: 13px; }
  .brand--front .brand-tagline { font-size: 10px; margin-top: 4px; }
</style>
</head>
<body>
<main class="canvas">
  <section class="spread" aria-label="Valtoria bifold brochure, outside spread">

    <article class="panel panel--back">
      <div class="meeting-photo" role="img" aria-label="Photo: silhouettes of business people shaking hands in a glass-walled meeting room"></div>
      <div class="cta-block">
        <p class="cta-text">What are you<br>waiting for?<br>Contact us now!</p>
      </div>
      <div class="brand brand--back">
        <div class="brand-name"><span>valtoria</span><span class="brand-mark"></span></div>
        <div class="brand-tagline">Plan Well. Buy Smart. Grow Steady.</div>
      </div>
      <div class="contact-column">
        <p class="contact-heading">Contact //</p>
        <p><span class="label">Address :</span> 1280 Harbor Row</p>
        <p>Suite 210, Marlow City, ST 40120</p>
        <p><span class="label">Phone:</span> 1-800-555-0142</p>
        <p><span class="label">Fax:</span> (800) 555-0199</p>
        <p><span class="label">E-mail:</span> hello@valtoriagroup.com</p>
        <span class="url-tag">www.valtoriagroup.com</span>
      </div>
    </article>

    <article class="panel panel--front">
      <div class="team-photo" role="img" aria-label="Photo: smiling businesswoman with arms crossed in front of a business team, world map backdrop"></div>
      <span class="url-tag front-url">www.valtoriagroup.com</span>
      <svg class="shapes" viewBox="0 0 500 700" aria-hidden="true">
        <polygon points="0,400 239,400 500,520 500,700 0,700" fill="var(--paper)"/>
        <polygon points="239,400 500,400 500,520" fill="var(--charcoal)"/>
        <polygon points="0,290 500,520 500,700 470,700 0,470" fill="var(--red-deep)"/>
        <polygon points="0,470 300,617 0,560" fill="var(--charcoal)"/>
      </svg>
      <h1 class="program-title">Vendor<br>Management<br>Program</h1>
      <div class="brand brand--front">
        <div class="brand-name"><span>valtoria</span><span class="brand-mark"></span></div>
        <div class="brand-tagline">Plan Well. Buy Smart. Grow Steady.</div>
      </div>
    </article>

  </section>
</main>
</body>
</html>
```